MoonPebble Radio - Spring Sessions DJ Dates

I've got a twice monthly DJ gig at a cafe coming up April - June and want a poster that's going to make people think - 'I want to go to that!'

I run an online radioshow (www.moonpebbleradio-fm.net) which specialises in soul, jazz, funk, hiphop, disco edits and anything that falls under the giant umbrella of Balearic. Check the site the Pinfolio which should give you a good idea of where we're at with MPBR: http://moonpebbleradio.pinfolio.net/. The gig at the cafe is all about the Soul/Jazz/Funk though, so I want to the poster to focus on that.

Influence: Jazz/Soul/Funk gig posters with head shots. Dorian Kettlewell blowing Sax. Noor wailing. Gideon singing into mic. Vinyl. Feeling: er, jazz/soul/funk - the classic. nb. can be obscure artists - feeling is more that the DJing is going to be hitting black US music 1960s-1980s. Points for quality obscure - track down anyone who's worked with Harold Quimby :)

Colours. Two/three tone. Black plus? White plus? Needs to make an effect from distance (location: front window of the pub, plus all over town). So it needs to be relatively simple.

Size: A2

There are bits that need to go on there - the MPBRadio logo for a start. Will send the files for that. Title: 'The MoonPebbleRadio Sessions'. Subtitles: 'At Muziekcafe Vlinder', 'With Mr. Lark.'

Then I got venue details and logo inc. friendwall, web addresses (the cafe and moonpebbleradio), my DJ name ' Mr Lark' and, most importantly, six dates and times. But they can come later - just important to note that there will need to be space somewhere for them.

Target Market(s)

All ages - cafe's clientele are late twenties and up. Not just specialist soul/funk heads. But music lovers.

Industry/Entity Type

Artists

Requirements
Must have
• Title and subtitles. MPBR Logo. Space for additional dates/info etc.
Should not have
• Think a bit broader than just someone with a big Afro. Not that I have anything against Afros, they rule. I've just seen a lot of posters advertising nights called 'Hat Parade' etc.

```html
<!DOCTYPE html>
<html lang="en">
<head>
<meta charset="utf-8">
<title>MoonPebble Radio Sessions – Soul/Jazz/Funk with Mr. Lark</title>
<link href="https://fonts.googleapis.com/css2?family=Anton&family=Audiowide&family=Oswald:wght@400;600&family=Pacifico&display=swap" rel="stylesheet">
<style>
  :root{
    --ink:#0b0b0c;
    --smoke:#2a2a2d;
    --white:#f2f2f0;
    --soft:#c9c9c6;
    --blue:#3fa4e6;
    --blue-glow:rgba(63,164,230,.75);
    --warm:#c8781f;
    --violet:#5b2a86;
  }
  *{margin:0;padding:0;box-sizing:border-box}
  html,body{width:874px;height:1200px;overflow:hidden;background:var(--ink)}
  .poster{
    position:relative;width:874px;height:1200px;overflow:hidden;
    background:
      radial-gradient(ellipse 70% 45% at 50% 0%, #4a4a4e 0%, var(--smoke) 40%, var(--ink) 100%);
    color:var(--white);
    font-family:"Oswald",sans-serif;
  }
  .title{
    position:absolute;top:28px;left:0;width:100%;
    text-align:center;
    font-family:"Anton",sans-serif;
    text-transform:uppercase;
    color:var(--white);
    line-height:.98;
    letter-spacing:2px;
  }
  .title__line{display:block;font-size:128px}
  .title__line--sm{font-size:118px}
  .sessions{
    position:absolute;top:418px;left:0;width:100%;text-align:center;
    font-family:"Audiowide",sans-serif;
    font-size:68px;color:var(--blue);
    text-shadow:0 0 14px var(--blue-glow),0 0 30px var(--blue-glow);
    line-height:1;
  }
  .genres{
    position:absolute;top:498px;left:0;width:100%;text-align:center;
    font-size:30px;font-weight:600;letter-spacing:1px;color:var(--white);
  }
  .with{
    position:absolute;top:538px;left:0;width:100%;text-align:center;
    font-size:24px;color:var(--soft);
  }
  .host{
    position:absolute;top:570px;left:0;width:100%;text-align:center;
    font-family:"Anton",sans-serif;font-size:46px;letter-spacing:2px;
    color:var(--white);
  }
  .artists{
    position:absolute;left:0;top:690px;width:874px;height:420px;
    background:
      radial-gradient(ellipse 30% 45% at 70% 45%, rgba(200,120,31,.55), transparent 70%),
      radial-gradient(ellipse 25% 40% at 88% 50%, rgba(91,42,134,.6), transparent 70%),
      radial-gradient(ellipse 45% 50% at 40% 55%, rgba(80,80,84,.6), transparent 75%),
      linear-gradient(180deg, transparent 0%, rgba(20,20,22,.8) 40%, var(--ink) 100%);
  }
  .dates{
    position:absolute;left:70px;top:990px;
    font-size:22px;line-height:1.3;
  }
  .dates__lead{font-size:22px;letter-spacing:1px;color:var(--white);margin-bottom:4px}
  .dates__row{display:flex;align-items:baseline;gap:14px;color:var(--white)}
  .dates__month{
    font-family:"Pacifico",cursive;color:var(--blue);
    font-size:26px;width:70px;
    text-shadow:0 0 8px var(--blue-glow);
  }
  .venue{
    position:absolute;left:300px;top:1160px;
    font-size:24px;color:var(--white);letter-spacing:.5px;
  }
  .brand{
    position:absolute;right:28px;top:1000px;width:150px;
    display:flex;flex-direction:column;align-items:center;gap:8px;
    text-align:center;
  }
  .brand__dot{width:70px;height:70px;border-radius:50%;background:var(--white)}
  .brand__name{
    font-family:"Oswald",sans-serif;font-weight:600;font-size:20px;
    line-height:1.05;color:var(--white);text-transform:uppercase;
  }
  .links{
    position:absolute;right:22px;top:1140px;text-align:right;
    font-size:15px;line-height:1.35;color:var(--soft);
  }
</style>
</head>
<body>
<main class="poster">
  <h1 class="title">
    <span class="title__line">Moon</span>
    <span class="title__line title__line--sm">Pebble</span>
    <span class="title__line">Radio</span>
  </h1>
  <p class="sessions">sessions</p>
  <p class="genres">soul/jazz/funk</p>
  <p class="with">with</p>
  <p class="host">MR. LARK</p>

  <div class="artists" role="img" aria-label="Collage of classic soul, jazz and funk performers: a trumpet player, a singer, a bassist and a vocalist with turntables, lit in warm and violet tones"></div>

  <section class="dates">
    <p class="dates__lead">TWICE MONTHLY</p>
    <p class="dates__row"><span class="dates__month">April</span><span>Sunday 14th . Friday 26th</span></p>
    <p class="dates__row"><span class="dates__month">May</span><span>Sunday 26th . Friday 31st</span></p>
    <p class="dates__row"><span class="dates__month">June</span><span>Sunday 23rd . Friday 28th</span></p>
  </section>
  <p class="venue">at Muziekcafe Vlinder</p>

  <div class="brand">
    <span class="brand__dot"></span>
    <span class="brand__name">MoonPebble Radio</span>
  </div>
  <p class="links">www.moonpebbleradio-fm.net<br>visit: www.friendwall.com</p>
</main>
</body>
</html>
```